Flyer for Medical practice welcoming new patients

We need a DL size brochure designed for Medical practice to advertise that we are accepting new patients. Our practice has special interests in women's and children's health and seniors health. Our existing advertising materials are in the colour scheme of purples I have uploaded our logo which includes our colour scheme.

Target Market(s)

Versatile to target anyone looking for a small medical practice that offers continuous care of seeing the same Doctor every time

Industry/Entity Type

Advertising

Font styles to use
Serif

Colors
6b449b
876aae
b7a5cc

Requirements
Must have
• The practice logo of just the picture not Dr Marla Thorncroft.
• Purple colour scheme.
• Practice name: Larkhaven Medical Practice.
• Address: 147 Tremont Rd, Larkhaven NSW 2500.
• Phone: 4873 6159.
• DL size brochure
• Welcoming new patients ( a strong emphasis needs to be placed on this)
• Nurse and onsite ECG's and lung function tests.
• Travel vaccines including yellow fever
• Bulk billing for tertiary students
• We would also like design to alter the text so that we can change the points to be reflect who we are targeting at the time.
Nice to have
• The practice logo with Dr Marla Thorncroft somewhere not as a feature as the practice no longer goes under this name but is still well known as Dr Thorncroft's.

```html
<!DOCTYPE html>
<html lang="en">
<head>
<meta charset="utf-8">
<title>Larkhaven Medical Practice – Accepting New Patients</title>
<link rel="stylesheet" href="https://fonts.googleapis.com/css2?family=Tinos&family=Didact+Gothic&family=Open+Sans:wght@400&display=swap">
<style>
  :root {
    --purple-deep: #6b449b;
    --purple-mid: #876aae;
    --purple-soft: #b7a5cc;
    --purple-text: #7656a4;
    --rule: #cdbfdd;
    --white: #ffffff;
    --sky-light: #eef2f6;
    --sky-mid: #d5dde6;
    --sky-deep: #b9c4d0;
  }
  html, body {
    margin: 0;
    padding: 0;
    width: 1200px;
    height: 600px;
    overflow: hidden;
    background: var(--white);
  }
  .flyer {
    position: relative;
    width: 1200px;
    height: 600px;
    overflow: hidden;
    background: var(--white);
  }
  .hero-photo {
    position: absolute;
    inset: 0;
    background:
      radial-gradient(ellipse 420px 520px at 1000px 260px, rgba(185,196,208,0.55), rgba(185,196,208,0) 70%),
      linear-gradient(90deg, var(--white) 0%, var(--white) 30%, var(--sky-light) 52%, var(--sky-mid) 78%, var(--sky-deep) 100%);
  }
  .practice-name {
    position: absolute;
    top: 22px;
    left: 0;
    width: 1200px;
    margin: 0;
    text-align: center;
    font-family: "Tinos", "Times New Roman", serif;
    font-weight: 400;
    font-size: 88px;
    letter-spacing: -1px;
    color: var(--purple-deep);
  }
  .services {
    position: absolute;
    top: 222px;
    left: 36px;
    display: grid;
    grid-template-columns: 246px 246px;
    column-gap: 34px;
    row-gap: 26px;
    margin: 0;
    padding: 0;
    list-style: none;
  }
  .service {
    font-family: "Didact Gothic", "Century Gothic", sans-serif;
    font-size: 25px;
    line-height: 28px;
    color: var(--purple-text);
    padding-bottom: 14px;
    border-bottom: 1.5px solid var(--rule);
    height: 84px;
    box-sizing: content-box;
  }
  .legacy-name {
    position: absolute;
    top: 424px;
    left: 516px;
    display: flex;
    align-items: center;
    gap: 14px;
  }
  .legacy-name .dot {
    width: 54px;
    height: 54px;
    border-radius: 50%;
    border: 2px solid var(--purple-soft);
    box-sizing: border-box;
  }
  .legacy-name .name {
    font-family: "Tinos", "Times New Roman", serif;
    font-size: 30px;
    color: var(--purple-mid);
  }
  .contact-band {
    position: absolute;
    left: 0;
    bottom: 0;
    width: 1200px;
    height: 70px;
    background: linear-gradient(90deg, var(--purple-deep) 0%, var(--purple-mid) 100%);
    border-top: 7px solid var(--purple-soft);
    box-sizing: border-box;
    display: flex;
    align-items: center;
    justify-content: flex-end;
    padding-right: 28px;
  }
  .contact-band p {
    margin: 0;
    font-family: "Open Sans", Arial, sans-serif;
    font-size: 26px;
    color: var(--white);
    letter-spacing: 0.2px;
  }
  .contact-band .sep {
    margin: 0 16px;
  }
</style>
</head>
<body>
  <main class="flyer">
    <div class="hero-photo" role="img" aria-label="Soft-focus photo of a doctor in a white coat with a stethoscope, holding a clipboard and pen"></div>

    <h1 class="practice-name">Larkhaven Medical Practice</h1>

    <ul class="services">
      <li class="service">accepting<br>new<br>patients</li>
      <li class="service">travel vaccines<br>including<br>yellow fever</li>
      <li class="service">onsite ECG's<br>and lung<br>function tests</li>
      <li class="service">bulk billing<br>for tertiary<br>students</li>
    </ul>

    <div class="legacy-name">
      <span class="dot"></span>
      <span class="name">Dr Marla Thorncroft</span>
    </div>

    <footer class="contact-band">
      <p>147 Tremont Rd, Larkhaven NSW 2500<span class="sep">|</span>phone 4873 6159</p>
    </footer>
  </main>
</body>
</html>
```